Construction company looking for modern

**Tallow Crest Joinery Limited**

We need a website for a renovation/remodeling company based in Hamilton, New Zealand. Ideally it will catch clients' attention and be modern and professional looking. I have attached a logo that I have just recently had made (through PixelHarbor). If the website could reflect this style and colour schemes, that would be awesome. The final design should communicate a trustworthiness and professionalism.

I have attached photos of a website that I really think is great, so if we could have something that follows along those likes,

https://www.dailyplover.example/local-news/news/local-builder-named-top-apprentice-for-region/QZTRPLA8VXN2MJ5DFYUEKHSWGO/

I won a competition a few years ago while I was an apprentice, If we could somehow put that in there as one of my achievements to try to bring in some trust that would be awesome. I would like to add a new picture though because my beard in that photo is wild.

Target Market(s)

Families that want live in the homes that i'm working on. not investors. People that are looking for quality not cheapest price.

Industry/Entity Type

Construction, Home renovations, Maintenance, Deck Builds, New Builds, Bathrooms, Kitchens

Coding

Coded - Design and coding required

Number of Pages Required

5+ page

Font styles to use
Sans Serif

Colors
6B429C
8869AF
B7A5CE
E3DAEB
F3F0F8

Requirements
Must have
• Contact us page, large clear pictures, Colours the work with the purple in my logo. That will be my company colour so I'm thinking black and purple, or what ever compliments purple nicely
Nice to have
• Page for Renovations, Testimonials, Contact us, Home, About us
Should not have
• Plain looking pages, empty white space, I want the text to be beside a nice big picture etc

```html
<!DOCTYPE html>
<html lang="en">
<head>
<meta charset="utf-8">
<title>Tallow Crest Joinery LTD — Home Renovations</title>
<link href="https://fonts.googleapis.com/css2?family=Poppins:wght@400;500;600;700&display=swap" rel="stylesheet">
<style>
:root{
  --purple:#6B429C;
  --purple-mid:#8869AF;
  --purple-soft:#B7A5CE;
  --purple-pale:#E3DAEB;
  --purple-tint:#F3F0F8;
  --ink:#1b1b1f;
  --body:#4a4a52;
  --muted:#8a8a92;
  --sand:#f6f4f2;
  --line:#e4e2e6;
  --white:#ffffff;
  --star:#f2b415;
}
*{box-sizing:border-box;margin:0;padding:0}
html,body{width:1200px;height:5314px;overflow:hidden}
body{font-family:"Poppins",sans-serif;color:var(--body);background:var(--white);position:relative}
.abs{position:absolute}
.eyebrow{font-size:15px;font-weight:500;letter-spacing:1.5px;color:var(--purple);text-transform:uppercase;text-align:center;width:100%;left:0}
.title{font-size:30px;font-weight:600;color:var(--ink);text-align:center;width:100%;left:0;line-height:1.35}
.btn{display:flex;align-items:center;justify-content:center;background:var(--purple);color:var(--white);font-size:14px;font-weight:600;letter-spacing:1.5px;text-transform:uppercase}
.photo{border-radius:2px}

/* header */
.site-header{left:0;top:0;width:1200px;height:99px;background:var(--white)}
.brand{display:flex;align-items:center;gap:8px}
.brand-mark{width:14px;height:14px;background:var(--purple)}
.brand-name{font-size:15px;font-weight:600;color:var(--purple);line-height:1.15}
.nav{left:352px;top:48px;display:flex;font-size:13px;font-weight:500;letter-spacing:1px;color:var(--ink)}
.nav span{margin-right:46px}
.nav span.tight{margin-right:24px}
.call{left:905px;top:36px;display:flex;align-items:center;gap:12px}
.call-icon{width:40px;height:40px;border-radius:50%;background:var(--purple);display:flex;align-items:center;justify-content:center}
.call small{display:block;font-size:12px;color:var(--muted)}
.call strong{display:block;font-size:17px;font-weight:600;color:var(--ink);letter-spacing:.5px}

/* hero */
.hero{left:0;top:99px;width:1200px;height:495px;
  background:
    linear-gradient(90deg,rgba(22,19,16,.78) 0%,rgba(22,19,16,.55) 38%,rgba(22,19,16,.12) 65%,rgba(22,19,16,0) 100%),
    linear-gradient(180deg,rgba(0,0,0,0) 55%,rgba(70,68,66,.55) 72%,rgba(40,38,36,.7) 100%),
    radial-gradient(ellipse 260px 200px at 760px 110px,rgba(214,170,118,.75),rgba(214,170,118,0)),
    radial-gradient(ellipse 300px 220px at 1060px 170px,rgba(236,230,220,.9),rgba(236,230,220,0)),
    linear-gradient(90deg,#6b5a48 0%,#8d7760 40%,#b9a488 70%,#ddd5c8 100%)}
.hero-label{left:124px;top:150px;font-size:16px;letter-spacing:2px;color:#f0ece8;font-weight:500}
.hero-title{left:124px;top:180px;width:560px;font-size:41px;font-weight:600;line-height:1.22;color:var(--white)}
.hero .btn{left:124px;top:367px;width:144px;height:41px}

/* about */
.about-photo{left:142px;top:841px;width:430px;height:429px;
  background:
    radial-gradient(ellipse 130px 210px at 200px 290px,rgba(96,128,92,.95),rgba(96,128,92,0)),
    radial-gradient(ellipse 70px 70px at 200px 110px,rgba(176,128,96,.85),rgba(176,128,96,0)),
    linear-gradient(90deg,#cfcac2 0%,#ece9e4 30%,#f4f2ee 65%,#d9d4cc 100%)}
.award{left:134px;top:1258px;width:124px;height:124px;border-radius:50%;background:#1c1a18;border:5px solid var(--white);box-shadow:0 4px 12px rgba(0,0,0,.2)}
.award::after{content:"";position:absolute;left:22px;top:22px;width:70px;height:70px;border-radius:50%;background:#c69a3a}
.owner-name{left:281px;top:1298px;font-size:24px;font-weight:600;color:var(--ink)}
.owner-note{left:281px;top:1336px;font-size:12px;color:var(--body);line-height:1.65}
.about-text{left:627px;top:832px;width:432px;font-size:13px;line-height:1.65;color:var(--body)}
.about-room{left:627px;top:1002px;width:431px;height:371px;
  background:
    radial-gradient(ellipse 60px 55px at 160px 215px,rgba(236,140,60,.9),rgba(236,140,60,0)),
    linear-gradient(180deg,rgba(0,0,0,0) 60%,rgba(90,88,92,.75) 85%,rgba(70,66,64,.9) 100%),
    linear-gradient(90deg,#b7a992 0%,#e3dccf 35%,#d8cfbf 60%,#a89d8c 100%)}

/* services */
.services-band{left:0;top:1619px;width:1200px;height:653px;
  background:
    radial-gradient(ellipse 220px 110px at 110px 600px,rgba(168,138,96,.9),rgba(168,138,96,0)),
    radial-gradient(ellipse 480px 180px at 600px 530px,rgba(150,150,150,.75),rgba(150,150,150,0)),
    radial-gradient(ellipse 240px 140px at 980px 560px,rgba(120,118,114,.8),rgba(120,118,114,0)),
    linear-gradient(180deg,#f7f6f4 0%,#ecebe8 40%,#dddad5 70%,#c9c4bc 100%)}
.service-card{top:1639px;width:291px;height:357px}
.service-card .overlay{position:absolute;inset:0;background:linear-gradient(180deg,rgba(0,0,0,0) 55%,rgba(0,0,0,.55))}
.service-card h3{position:absolute;left:21px;bottom:22px;font-size:18px;font-weight:600;letter-spacing:1.5px;color:var(--white);line-height:1.3;text-transform:uppercase}
.service-card svg{position:absolute;right:20px;bottom:24px}
.svc-1{left:142px;background:
  linear-gradient(90deg,#cfcac4 0%,#eeece8 30%,#d9d3cb 60%,#8e5a44 80%,#6d4a3a 100%)}
.svc-2{left:454px;background:
  radial-gradient(ellipse 60px 80px at 200px 110px,rgba(104,128,82,.85),rgba(104,128,82,0)),
  radial-gradient(ellipse 110px 70px at 220px 290px,rgba(176,140,104,.9),rgba(176,140,104,0)),
  linear-gradient(90deg,#8f8c88 0%,#b8b6b2 40%,#d6d4d0 100%)}
.svc-3{left:767px;background:
  radial-gradient(ellipse 150px 90px at 150px 260px,rgba(178,172,164,.9),rgba(178,172,164,0)),
  linear-gradient(90deg,#6e6d6b 0%,#cfcdc9 25%,#efeeec 60%,#dcdad6 100%)}
.all-services{left:526px;top:2047px;width:148px;height:48px}

/* mission */
.mission{left:0;top:2272px;width:1200px;height:635px;background:var(--sand)}
.mission-text{left:180px;top:2469px;width:840px;text-align:center;font-size:14px;line-height:1.75;color:var(--ink)}
.value-card{top:2581px;width:217px;height:238px;background:var(--purple);display:flex;flex-direction:column;align-items:center}
.value-card .disc{margin-top:28px;width:112px;height:112px;border-radius:50%;background:var(--white);display:flex;align-items:center;justify-content:center}
.value-card h4{margin-top:24px;text-align:center;font-size:14px;font-weight:600;letter-spacing:.8px;color:var(--white);line-height:1.45;text-transform:uppercase}

/* testimonials */
.avatar{width:82px;height:82px;border-radius:50%}
.quote{width:340px}
.stars{display:flex;gap:5px;margin-bottom:12px}
.quote p{font-size:13px;line-height:1.65;color:var(--body)}
.quote .who{margin-top:22px;margin-left:22px;font-size:13px;font-weight:600;color:var(--purple)}
.quote .who::before{content:"";display:inline-block;width:16px;height:1px;background:var(--purple);vertical-align:middle;margin-right:8px}
.quote .where{margin-left:46px;font-size:11px;color:var(--muted)}
.dots{left:540px;top:3327px;display:flex;align-items:center;gap:16px}
.dots i{width:9px;height:9px;border-radius:50%;background:#d6d3da;display:block}
.dots i.on{width:18px;height:18px;background:var(--white);border:2px solid var(--purple);position:relative}
.dots i.on::after{content:"";position:absolute;left:3px;top:3px;width:8px;height:8px;border-radius:50%;background:var(--purple)}

/* gallery */
.project{width:291px}
.project .shot{height:250px}
.project h5{margin-top:27px;font-size:18px;font-weight:600;letter-spacing:1px;color:var(--ink);line-height:1.35}
.shot-1{background:
  radial-gradient(ellipse 90px 60px at 140px 175px,rgba(196,150,100,.95),rgba(196,150,100,0)),
  radial-gradient(ellipse 120px 50px at 150px 140px,rgba(190,190,188,.9),rgba(190,190,188,0)),
  linear-gradient(90deg,#8a6d52 0%,#cbb79c 30%,#e6e0d6 65%,#d4d8dc 100%)}
.shot-2{background:
  radial-gradient(ellipse 70px 60px at 160px 60px,rgba(40,36,34,.85),rgba(40,36,34,0)),
  radial-gradient(ellipse 150px 45px at 150px 155px,rgba(220,214,200,.95),rgba(220,214,200,0)),
  linear-gradient(180deg,#e4dbcd 0%,#d8cdbb 55%,#a49684 80%,#c9bcaa 100%)}
.shot-3{background:
  radial-gradient(ellipse 80px 90px at 220px 80px,rgba(96,150,200,.9),rgba(96,150,200,0)),
  radial-gradient(ellipse 120px 60px at 170px 200px,rgba(70,70,74,.7),rgba(70,70,74,0)),
  linear-gradient(90deg,#e6e6e4 0%,#f2f2f0 45%,#cfd6dc 100%)}
.shot-4{background:
  radial-gradient(ellipse 140px 60px at 170px 180px,rgba(194,100,52,.95),rgba(194,100,52,0)),
  radial-gradient(ellipse 50px 110px at 80px 90px,rgba(38,56,96,.9),rgba(38,56,96,0)),
  linear-gradient(90deg,#d8dadc 0%,#b8b4ae 45%,#9a948c 100%)}
.shot-5{background:
  radial-gradient(ellipse 90px 50px at 140px 170px,rgba(226,220,210,.95),rgba(226,220,210,0)),
  radial-gradient(ellipse 70px 130px at 250px 130px,rgba(196,160,128,.8),rgba(196,160,128,0)),
  linear-gradient(90deg,#f1efec 0%,#f7f5f2 50%,#e4dccf 100%)}
.shot-6{background:
  radial-gradient(ellipse 80px 30px at 90px 40px,rgba(210,170,90,.85),rgba(210,170,90,0)),
  radial-gradient(ellipse 130px 60px at 120px 185px,rgba(52,56,70,.9),rgba(52,56,70,0)),
  linear-gradient(90deg,#4d4c50 0%,#6b6a6e 45%,#a09890 100%)}

/* contact */
.contact{left:0;top:4305px;width:1200px;height:619px;
  background:
    radial-gradient(ellipse 320px 130px at 980px 560px,rgba(140,84,44,.85),rgba(140,84,44,0)),
    radial-gradient(ellipse 260px 200px at 180px 200px,rgba(120,104,92,.7),rgba(120,104,92,0)),
    linear-gradient(180deg,#3d3530 0%,#2c2622 55%,#3f3128 100%)}
.form-card{left:173px;top:4479px;width:835px;height:299px;background:var(--white)}
.input{height:39px;width:382px;border-bottom:1px solid var(--line);border-left:1px solid var(--line);border-top:1px solid var(--line);font-size:13px;padding:14px 0 0 6px;color:var(--ink)}
.textarea{left:604px;top:4522px;width:365px;height:159px;border:1px solid var(--line);font-size:13px;padding:14px 0 0 20px;color:var(--ink)}
.submit{left:526px;top:4699px;width:148px;height:48px}

/* footer */
.site-footer{left:0;top:4924px;width:1200px;height:390px;background:var(--white)}
.foot-brand{left:150px;top:5036px}
.socials{left:168px;top:5136px;display:flex;gap:8px}
.socials i{display:block;width:26px;height:26px;border-radius:50%;background:var(--ink)}
.socials i.mid{background:var(--purple)}
.foot-col{top:4992px;border-left:2px solid var(--purple);padding-left:22px;height:200px}
.foot-col h6{font-size:14px;font-weight:600;letter-spacing:.5px;color:var(--ink);margin-bottom:22px;text-transform:uppercase}
.foot-col li{list-style:none;font-size:13px;color:var(--body);margin-bottom:13px}
.contact-row{display:flex;gap:18px;align-items:flex-start;font-size:13px;color:var(--body);line-height:1.4;margin-bottom:16px}
.contact-row svg{flex:none;margin-top:2px}
.foot-rule{left:148px;top:5248px;width:904px;height:1px;background:var(--line)}
.copyright{left:0;top:5270px;width:1200px;text-align:center;font-size:13px;color:var(--body)}
</style>
</head>
<body>

<header class="site-header abs">
  <div class="brand abs" style="left:120px;top:38px">
    <span class="brand-mark"></span>
    <span class="brand-name">Tallow Crest<br>Joinery LTD</span>
  </div>
  <nav class="nav abs">
    <span>HOME</span><span>ABOUT US</span><span class="tight">SERVICES</span><span class="tight">TESTIMONIALS</span><span>CONTACT US</span>
  </nav>
  <div class="call abs">
    <div class="call-icon">
      <svg width="18" height="18" viewBox="0 0 24 24" fill="#fff"><path d="M6.6 10.8a15.1 15.1 0 0 0 6.6 6.6l2.2-2.2c.3-.3.7-.4 1-.2 1.1.4 2.3.6 3.6.6.6 0 1 .4 1 1V20c0 .6-.4 1-1 1A17 17 0 0 1 3 4c0-.6.4-1 1-1h3.5c.6 0 1 .4 1 1 0 1.3.2 2.5.6 3.6.1.3 0 .7-.2 1z"/></svg>
    </div>
    <div><small>Call Us</small><strong>(027) 555-0143</strong></div>
  </div>
</header>

<section class="hero abs" role="img" aria-label="Photo of a bright open-plan renovated living room with grey sofa and timber kitchen">
  <p class="hero-label abs">TALLOW CREST JOINERY LTD</p>
  <h1 class="hero-title abs">Your Trusted Partner in Home Renovations and Building Excellence</h1>
  <div class="btn abs">Contact Us</div>
</section>

<p class="eyebrow abs" style="top:666px">About Us</p>
<h2 class="title abs" style="top:700px">Bringing Your Vision to Life with Quality<br>Renovations and Construction</h2>
<div class="about-photo abs photo" role="img" aria-label="Photo of the company owner standing in a doorway of a renovated living room"></div>
<div class="award abs" role="img" aria-label="Apprentice award medal"></div>
<p class="owner-name abs">Marlon Keswick</p>
<p class="owner-note abs">"The region's top building apprentice"<br>at the Regional Builders Apprentice Challenge</p>
<p class="about-text abs">At Tallow Crest Joinery LTD, we take pride in our ability to turn your dreams into reality. Our commitment to quality and dedication to craftsmanship are the cornerstones of our service. With years of experience, a winning spirit, and a passion for creating exceptional living spaces, we are your trusted partner in home renovations and construction.</p>
<div class="about-room abs photo" role="img" aria-label="Photo of a cosy living room with fireplace and grey sofas"></div>

<p class="eyebrow abs" style="top:1525px">Services</p>
<h2 class="title abs" style="top:1553px">Our Comprehensive Services</h2>
<div class="services-band abs" role="img" aria-label="Soft background photo of a bright bedroom with a grey bed and ottoman"></div>
<article class="service-card svc-1 abs" role="img" aria-label="Photo of a renovated hallway with brick wall and staircase">
  <div class="overlay"></div><h3>Home<br>Renovations</h3>
  <svg width="32" height="32" viewBox="0 0 32 32" fill="none" stroke="#fff" stroke-width="1.6"><circle cx="16" cy="16" r="14"/><path d="M10 16h12M17 11l5 5-5 5"/></svg>
</article>
<article class="service-card svc-2 abs" role="img" aria-label="Photo of a modern bathroom with glass shower and timber vanity">
  <div class="overlay"></div><h3>Bathrooms</h3>
  <svg width="32" height="32" viewBox="0 0 32 32" fill="none" stroke="#fff" stroke-width="1.6"><circle cx="16" cy="16" r="14"/><path d="M10 16h12M17 11l5 5-5 5"/></svg>
</article>
<article class="service-card svc-3 abs" role="img" aria-label="Photo of a minimalist grey kitchen with island bench">
  <div class="overlay"></div><h3>Kitchens</h3>
  <svg width="32" height="32" viewBox="0 0 32 32" fill="none" stroke="#fff" stroke-width="1.6"><circle cx="16" cy="16" r="14"/><path d="M10 16h12M17 11l5 5-5 5"/></svg>
</article>
<div class="btn abs all-services">All Services</div>

<section class="mission abs"></section>
<p class="eyebrow abs" style="top:2369px">Mission</p>
<h2 class="title abs" style="top:2397px">Your Vision, Our Expertise</h2>
<p class="mission-text abs">At Tallow Crest Joinery LTD, we understand that our target market consists of families seeking quality homes, not just investors looking for a quick profit. We know that your home is more than just a building; it's where you create cherished memories and lay the foundation for your family's future. That's why we offer:</p>
<div class="value-card abs" style="left:140px">
  <div class="disc"><svg width="62" height="62" viewBox="0 0 64 64" fill="none" stroke="#6B429C" stroke-width="2.5" stroke-linejoin="round"><path d="M10 32 32 14l22 18"/><path d="M16 28v24h32V28"/><path d="M27 52V39h10v13"/><path d="M40 10l10 10-4 4-10-10z"/></svg></div>
  <h4>Customized<br>Solutions</h4>
</div>
<div class="value-card abs" style="left:373px">
  <div class="disc"><svg width="62" height="62" viewBox="0 0 64 64" fill="none" stroke="#6B429C" stroke-width="2.5"><circle cx="32" cy="32" r="22"/><circle cx="32" cy="32" r="15"/><path d="m25 32 5 5 10-10"/></svg></div>
  <h4>Quality<br>Craftsmanship</h4>
</div>
<div class="value-card abs" style="left:608px">
  <div class="disc"><svg width="62" height="62" viewBox="0 0 64 64" fill="none" stroke="#6B429C" stroke-width="2.5" stroke-linejoin="round"><rect x="12" y="12" width="40" height="30"/><path d="M22 42v8h20v-8M20 20h24v14H20z"/><path d="M28 27h8M14 54h36"/></svg></div>
  <h4>Attention To<br>Detail</h4>
</div>
<div class="value-card abs" style="left:841px">
  <div class="disc"><svg width="62" height="62" viewBox="0 0 64 64" fill="none" stroke="#6B429C" stroke-width="2.5" stroke-linecap="round"><path d="M14 36v-6a18 18 0 0 1 36 0v6"/><rect x="10" y="34" width="9" height="14" rx="3"/><rect x="45" y="34" width="9" height="14" rx="3"/><path d="M50 48c0 5-6 8-14 8"/><circle cx="34" cy="56" r="2"/></svg></div>
  <h4>Expert<br>Consultation</h4>
</div>

<p class="eyebrow abs" style="top:2983px">Testimonials</p>
<h2 class="title abs" style="top:3011px">What our Customers Say</h2>
<div class="avatar abs" style="left:139px;top:3132px;background:radial-gradient(circle at 50% 40%,#e8d8c2,#b59878 70%,#8a7868)" role="img" aria-label="Customer portrait photo"></div>
<div class="quote abs" style="left:241px;top:3104px">
  <div class="stars">
    <svg width="20" height="19" viewBox="0 0 24 23"><path fill="#f2b415" d="m12 0 3.7 7.5 8.3 1.2-6 5.8 1.4 8.3L12 18.9l-7.4 3.9 1.4-8.3-6-5.8 8.3-1.2z"/></svg>
    <svg width="20" height="19" viewBox="0 0 24 23"><path fill="#f2b415" d="m12 0 3.7 7.5 8.3 1.2-6 5.8 1.4 8.3L12 18.9l-7.4 3.9 1.4-8.3-6-5.8 8.3-1.2z"/></svg>
    <svg width="20" height="19" viewBox="0 0 24 23"><path fill="#f2b415" d="m12 0 3.7 7.5 8.3 1.2-6 5.8 1.4 8.3L12 18.9l-7.4 3.9 1.4-8.3-6-5.8 8.3-1.2z"/></svg>
    <svg width="20" height="19" viewBox="0 0 24 23"><path fill="#f2b415" d="m12 0 3.7 7.5 8.3 1.2-6 5.8 1.4 8.3L12 18.9l-7.4 3.9 1.4-8.3-6-5.8 8.3-1.2z"/></svg>
    <svg width="20" height="19" viewBox="0 0 24 23"><path fill="#f2b415" d="m12 0 3.7 7.5 8.3 1.2-6 5.8 1.4 8.3L12 18.9l-7.4 3.9 1.4-8.3-6-5.8 8.3-1.2z"/></svg>
  </div>
  <p>"We couldn't be happier with the kitchen renovation Tallow Crest Joinery LTD completed for us. They took our vision and turned it into a reality, and the attention to detail was astounding."</p>
  <p class="who">Anna and Pete R.</p>
  <p class="where">Hamilton, NZ</p>
</div>
<div class="avatar abs" style="left:619px;top:3132px;background:radial-gradient(circle at 50% 40%,#7a7a82,#34343c 70%,#1e1e24)" role="img" aria-label="Customer portrait photo"></div>
<div class="quote abs" style="left:720px;top:3104px">
  <div class="stars">
    <svg width="20" height="19" viewBox="0 0 24 23"><path fill="#f2b415" d="m12 0 3.7 7.5 8.3 1.2-6 5.8 1.4 8.3L12 18.9l-7.4 3.9 1.4-8.3-6-5.8 8.3-1.2z"/></svg>
    <svg width="20" height="19" viewBox="0 0 24 23"><path fill="#f2b415" d="m12 0 3.7 7.5 8.3 1.2-6 5.8 1.4 8.3L12 18.9l-7.4 3.9 1.4-8.3-6-5.8 8.3-1.2z"/></svg>
    <svg width="20" height="19" viewBox="0 0 24 23"><path fill="#f2b415" d="m12 0 3.7 7.5 8.3 1.2-6 5.8 1.4 8.3L12 18.9l-7.4 3.9 1.4-8.3-6-5.8 8.3-1.2z"/></svg>
    <svg width="20" height="19" viewBox="0 0 24 23"><path fill="#f2b415" d="m12 0 3.7 7.5 8.3 1.2-6 5.8 1.4 8.3L12 18.9l-7.4 3.9 1.4-8.3-6-5.8 8.3-1.2z"/></svg>
    <svg width="20" height="19" viewBox="0 0 24 23"><path fill="#f2b415" d="m12 0 3.7 7.5 8.3 1.2-6 5.8 1.4 8.3L12 18.9l-7.4 3.9 1.4-8.3-6-5.8 8.3-1.2z"/></svg>
  </div>
  <p>"Tallow Crest Joinery LTD turned our house into a home. We entrusted them with a major renovation project, and the results were beyond our expectations."</p>
  <p class="who">Anna and Pete R.</p>
  <p class="where">Hamilton, NZ</p>
</div>
<div class="dots abs"><i></i><i></i><i class="on"></i><i></i><i></i></div>

<p class="eyebrow abs" style="top:3408px">Gallery</p>
<h2 class="title abs" style="top:3436px">Recent Projects</h2>
<div class="project abs" style="left:142px;top:3516px"><div class="shot shot-1" role="img" aria-label="Project photo of a living room with grey sofa and rattan lamp"></div><h5>A Stunning Kitchen<br>Renovation</h5></div>
<div class="project abs" style="left:454px;top:3516px"><div class="shot shot-2" role="img" aria-label="Project photo of a neutral lounge with artwork and rug"></div><h5>A Stunning Kitchen<br>Renovation</h5></div>
<div class="project abs" style="left:767px;top:3516px"><div class="shot shot-3" role="img" aria-label="Project photo of a white kitchen with bar stools and large windows"></div><h5>A Stunning Kitchen<br>Renovation</h5></div>
<div class="project abs" style="left:142px;top:3870px"><div class="shot shot-4" role="img" aria-label="Project photo of a bedroom with orange headboard and blue curtains"></div><h5>A Stunning Kitchen<br>Renovation</h5></div>
<div class="project abs" style="left:454px;top:3870px"><div class="shot shot-5" role="img" aria-label="Project photo of a bright dining area with white chairs"></div><h5>A Stunning Kitchen<br>Renovation</h5></div>
<div class="project abs" style="left:767px;top:3870px"><div class="shot shot-6" role="img" aria-label="Project photo of a dark grey bedroom with timber desk"></div><h5>A Stunning Kitchen<br>Renovation</h5></div>

<section class="contact abs" role="img" aria-label="Dark background photo of a living room with leather pouf"></section>
<p class="eyebrow abs" style="top:4382px;color:#fff">Contact Us</p>
<h2 class="title abs" style="top:4405px;color:#fff">Ready to Transform Your Space?</h2>
<form class="form-card abs"></form>
<div class="input abs" style="left:206px;top:4522px">Your name</div>
<div class="input abs" style="left:206px;top:4582px">Your phone</div>
<div class="input abs" style="left:206px;top:4641px">Your email</div>
<div class="textarea abs">Message here</div>
<div class="btn abs submit">Submit Now</div>

<footer class="site-footer abs"></footer>
<div class="brand foot-brand abs">
  <span class="brand-mark"></span>
  <span class="brand-name" style="font-size:18px">Tallow Crest<br>Joinery LTD</span>
</div>
<div class="socials abs"><i></i><i class="mid"></i><i></i></div>
<div class="foot-col abs" style="left:400px">
  <h6>Contact Information</h6>
  <div class="contact-row"><svg width="14" height="18" viewBox="0 0 14 18"><path fill="#6B429C" d="M7 0a7 7 0 0 0-7 7c0 5 7 11 7 11s7-6 7-11a7 7 0 0 0-7-7zm0 9.5A2.5 2.5 0 1 1 7 4.5a2.5 2.5 0 0 1 0 5z"/></svg><span>418 Harrow Lane,<br>Fernbrook 3204</span></div>
  <div class="contact-row"><svg width="14" height="14" viewBox="0 0 24 24"><path fill="#6B429C" d="M6.6 10.8a15.1 15.1 0 0 0 6.6 6.6l2.2-2.2c.3-.3.7-.4 1-.2 1.1.4 2.3.6 3.6.6.6 0 1 .4 1 1V20c0 .6-.4 1-1 1A17 17 0 0 1 3 4c0-.6.4-1 1-1h3.5c.6 0 1 .4 1 1 0 1.3.2 2.5.6 3.6.1.3 0 .7-.2 1z"/></svg><span>+64 7 555 0192</span></div>
  <div class="contact-row"><svg width="14" height="12" viewBox="0 0 14 12"><path fill="#6B429C" d="M0 0h14v12H0z"/><path fill="none" stroke="#fff" stroke-width="1.3" d="m1 1 6 5 6-5"/></svg><span>hello@tallowcrest.example</span></div>
</div>
<div class="foot-col abs" style="left:693px">
  <h6>Quick Links</h6>
  <ul><li>Home</li><li>About Us</li><li>Portfolio</li><li>Testimonials</li><li>Contact Us</li></ul>
</div>
<div class="foot-col abs" style="left:883px">
  <h6>Services</h6>
  <ul><li>Home Renovations</li><li>Maintenance</li><li>Deck Builds</li><li>Bathrooms</li><li>Kitchens</li><li>Customized Solutions</li></ul>
</div>
<div class="foot-rule abs"></div>
<p class="copyright abs">© 2023 All Rights Reserved | Tallow Crest Joinery LTD</p>

</body>
</html>
```